Brenner & Holloway Stationery

Greetings again. Now we've got an awesome logo, it's time to get the stationery to go with it. We require the following items of stationery:

- Business Card - Print Ready, all we need to do is change names and numbers and submit to printer.  Double sided with logo on one side and details on the other side. (85mm x 55mm)

- With Compliments Slip

- Letterhead - These will be preprinted pages that will then be used as pages.
(A4)

- Envelope - Business Size(Standard DL)

Target Market(s)

Essentially, this firm services clients facing criminal charges and/or seeking legal aid. The firm is also looking at taking on more white-collar crime cases.

Requirements
Must have
• - Same Design Cues & Colours as the Branding details attached

• - Address (as follows)

• Suite 8

• 262-268 Marlow St

• WESTHOLM VIC 3990

• Phone: (03) 9482 6315

• Fax: (03) 9482 6840

• Web: www.brennerandholloway.example.au

• - Colour: Pantone 194 (Red)

```html
<!DOCTYPE html>
<html lang="en">
<head>
<meta charset="utf-8">
<title>Brenner &amp; Holloway Stationery</title>
<link rel="stylesheet" href="https://fonts.googleapis.com/css2?family=EB+Garamond:wght@400;500;600&family=Pinyon+Script&display=swap">
<style>
  :root {
    --crimson: #a9003a;
    --ink: #231f20;
    --rule: #b3b3b3;
    --paper: #ffffff;
    --edge: #111111;
  }
  * { margin: 0; padding: 0; box-sizing: border-box; }
  html, body { width: 1007px; height: 1200px; overflow: hidden; background: var(--paper); }
  body { position: relative; font-family: "EB Garamond", Garamond, serif; color: var(--ink); }
  .piece { position: absolute; background: var(--paper); overflow: hidden; }
  .piece > * { position: absolute; line-height: 1; white-space: nowrap; }
  .card { width: 429px; height: 249px; border: 1px solid var(--edge); border-radius: 23px; }
  .letterhead { left: 477px; top: 4px; width: 521px; height: 674px; border: 1.7px solid var(--edge); border-radius: 23px; }
  .envelope { width: 513px; height: 221px; border: 1.7px solid var(--edge); }
  .slip { border: 1.7px solid var(--edge); border-radius: 7px; }
  .mark { border-radius: 50%; background: var(--crimson); }
  .divider { width: 1px; background: var(--rule); }
  .firm-name { font-weight: 500; font-variant: small-caps; color: var(--ink); letter-spacing: 0.02em; }
  .firm-role { font-weight: 500; text-transform: uppercase; letter-spacing: 0.14em; color: var(--ink); }
  .holder-name { color: var(--crimson); font-weight: 600; text-transform: uppercase; }
  .contact { font-size: 16px; }
  .small-print { font-size: 4.6px; line-height: 1.15; }
  .compliments { font-family: "Pinyon Script", cursive; color: var(--crimson); }
  .hr { height: 1.5px; background: var(--rule); }
  .flap { left: 0; top: 0; width: 100%; height: 85px; background: var(--crimson); border-radius: 0 0 11px 11px; }
  .flap-address { color: var(--paper); font-size: 8px; line-height: 1.05; text-align: center; width: 100%; left: 0; }
</style>
</head>
<body>

<!-- Business card: logo side -->
<section class="piece card" style="left:0; top:0;">
  <div class="mark" style="left:53px; top:81px; width:80px; height:80px;"></div>
  <div class="divider" style="left:149px; top:81px; height:81px;"></div>
  <div class="firm-name" style="left:165px; top:106px; font-size:21px;">Brenner &amp; Holloway</div>
  <div class="firm-role" style="left:165px; top:129px; font-size:10.5px;">Barristers &amp; Solicitors</div>
</section>

<!-- Business card: details side, compact lockup -->
<section class="piece card" style="left:0; top:298px;">
  <div class="mark" style="left:19px; top:18px; width:41px; height:41px;"></div>
  <div class="divider" style="left:68px; top:18px; height:40px;"></div>
  <div class="firm-name" style="left:76px; top:29px; font-size:13px;">Brenner &amp; Holloway</div>
  <div class="firm-role" style="left:76px; top:43px; font-size:6.4px;">Barristers &amp; Solicitors</div>

  <div class="holder-name" style="left:20px; top:85px; font-size:17px;">Holders Name</div>
  <div class="contact" style="left:20px; top:105px;">Holders Position</div>

  <div class="contact" style="left:200px; top:86px; line-height:18.5px;">Suite 8 - 262-268 Marlow St<br>WESTHOLM VIC 3990</div>
  <div class="contact" style="left:200px; top:141px; line-height:18.5px;">Phone: (03) 9482 6315<br>Fax: (03) 9482 6840</div>
  <div style="left:200px; top:181px; font-size:13.5px;">www.brennerandholloway.example.au</div>
</section>

<!-- Business card: alternative details side with large mark -->
<section class="piece card" style="left:4px; top:599px;">
  <div class="mark" style="left:14px; top:32px; width:182px; height:182px;"></div>
  <div class="holder-name" style="left:218px; top:28px; font-size:17px;">Holders Name</div>
  <div class="contact" style="left:218px; top:48px;">Holders Position</div>
  <div class="hr" style="left:218px; top:83px; width:193px;"></div>
  <div class="contact" style="left:218px; top:103px; line-height:18.5px;">Suite 8 - 262-268 Marlow St<br>WESTHOLM VIC 3990</div>
  <div class="contact" style="left:218px; top:159px; line-height:18.5px;">Phone: (03) 9482 6315<br>Fax: (03) 9482 6840</div>
  <div style="left:218px; top:199px; font-size:12.6px;">www.brennerandholloway.example.au</div>
</section>

<!-- A4 letterhead -->
<section class="piece letterhead">
  <div style="left:0; width:138px; top:73px; font-size:8.6px; line-height:9.5px; text-align:right;">Suite 8 - 262-268 Marlow St<br>WESTHOLM VIC 3990</div>
  <div class="mark" style="left:169px; top:57px; width:45px; height:45px;"></div>
  <div class="divider" style="left:223px; top:57px; height:45px;"></div>
  <div class="firm-name" style="left:231px; top:70px; font-size:13px;">Brenner &amp; Holloway</div>
  <div class="firm-role" style="left:231px; top:84px; font-size:6.4px;">Barristers &amp; Solicitors</div>
  <div style="left:382px; top:73px; font-size:8.6px; line-height:9.5px;">Phone: (03) 9482 6315<br>Fax: (03) 9482 6840</div>
  <div style="left:0; width:100%; top:645px; font-size:8.6px; text-align:center;">www.brennerandholloway.example.au</div>
</section>

<!-- DL envelope: front -->
<section class="piece envelope" style="left:486px; top:734px;">
  <div class="mark" style="left:11px; top:13px; width:36px; height:36px;"></div>
  <div class="divider" style="left:55px; top:13px; height:36px;"></div>
  <div class="firm-name" style="left:62px; top:24px; font-size:11.5px;">Brenner &amp; Holloway</div>
  <div class="firm-role" style="left:62px; top:36px; font-size:5.6px;">Barristers &amp; Solicitors</div>
</section>

<!-- DL envelope: back with flap -->
<section class="piece envelope" style="left:486px; top:978px;">
  <div class="flap"></div>
  <div class="flap-address" style="top:34px;">Suite 8 - 262-268 Marlow St<br>WESTHOLM VIC 3990</div>
</section>

<!-- With compliments slip: large mark -->
<section class="piece slip" style="left:15px; top:871px; width:231px; height:154px;">
  <div class="mark" style="left:8px; top:7px; width:58px; height:58px;"></div>
  <div class="compliments" style="left:140px; top:15px; font-size:13px;">With compliments</div>
  <div class="hr" style="left:140px; top:36px; width:80px; height:1px;"></div>
  <div class="small-print" style="left:10px; top:115px;">Suite 8 - 262-268 Marlow St<br>Westholm VIC 3990</div>
  <div class="small-print" style="left:10px; top:130px;">Phone: (03) 9482 6315<br>Fax: (03) 9482 6840<br>www.brennerandholloway.example.au</div>
</section>

<!-- With compliments slip: compact lockup -->
<section class="piece slip" style="left:203px; top:1040px; width:228px; height:152px;">
  <div class="mark" style="left:10px; top:15px; width:16px; height:16px;"></div>
  <div class="divider" style="left:30px; top:15px; height:16px;"></div>
  <div class="firm-name" style="left:33px; top:19px; font-size:5.4px;">Brenner &amp; Holloway</div>
  <div class="firm-role" style="left:33px; top:25px; font-size:2.7px;">Barristers &amp; Solicitors</div>
  <div class="compliments" style="right:10px; top:16px; font-size:13px;">With compliments</div>
  <div class="small-print" style="left:10px; top:116px;">Suite 8 - 262-268 Marlow St<br>Westholm VIC 3990</div>
  <div class="small-print" style="left:10px; top:130px;">Phone: (03) 9482 6315<br>Fax: (03) 9482 6840<br>www.brennerandholloway.example.au</div>
</section>

</body>
</html>
```